Facebook page as well as a business card and stationary design for a fitness instructor/personal trainer who is branching out as an independent worker delivering the gym experience (personal training or small group classes) to the home market. The trainer (LD or Lev Dunmore) is young, energetic, and results oriented.

Job Type
Facebook page and 2-sided business card
Task Outline
Create a Facebook presence (supported by a business card) for a train-you-at-home personal trainer
Task Description
Looking for a Graphic Designer/Web Designer to make a really modern/clean Facebook page that promotes Lev Dunmore ("LD") as at-your-home personal trainer. Lev's goal as a personal trainer is to motivate, inspire and educate all of his clients about the benefits of regular exercise, nourishing the body with nutritious foods, and living a healthy lifestyle while enjoying working out. He wants to encourage the convenience component of what he does by offering personal training sessions at a person's home or place of business. He trains both men and women, so the design of both the business card and the Facebook page should appeal to both genders and not come across as more feminine or more masculine. The Facebook page should include links to the Chirper, Instagram, and email accounts. It should also hold a placeholder link to his future web site called BougeAvecToi.

He holds several certifications and would like these mentioned on his Facebook page and perhaps on his business card -- either in text form or identifying them with the logos (which are attached).

Contact information for the business card will be supplied shortly. In the interim, the following can be used: Lev Dunmore Personal Trainer; Address: 47 Valmorin, Havre-Loriot, Belcourt, K7R 2P4, Email: ldstrongdaily@mailbox.example; Phone: 555.204-3917; Facebook: LDStrongDaily; Chirper: LDStrongDaily; Website: BougeAvecToi.example

OTHER INFORMATION: This project is a Christmas present to the personal trainer who is a friend. He'll be making the final decisions on the designs for both components.
Updates

Reason: I haven't given designers enough time to respond to my feedback. I apologize for any inconveniences. Best regard.

Target Market(s)

Both men and women who don't have the time for the gym and are looking for personal training at home or at their place of work.

Industry/Entity Type

Personal Trainer

Contact Information for Business Card

No photo. Clean lines and preference of blue colouring. contact information presented clearly. Card design must radiate the concept of fitness for life, living healthy and strong.

Font styles to use
Sans Serif

Colors
34a7d8
86cae6
85acd3
0355a3
0592ce
cee9f5
ceddec
86cfc6
cfeae6

```html
<!DOCTYPE html>
<html lang="en">
<head>
<meta charset="utf-8">
<title>Lev Dunmore – Home Personal Trainer</title>
<link rel="stylesheet" href="https://fonts.googleapis.com/css2?family=Bebas+Neue&family=Oswald:wght@500;700&family=Noto+Sans+Bengali:wght@400;600&display=swap">
<style>
:root{
  --stage:#262626;
  --brand-blue:#0b3f7e;
  --brand-blue-bright:#0355a3;
  --icon-blue:#1a4f90;
  --white:#ffffff;
  --silver-hi:#f4f4f4;
  --silver-lo:#9a9a9a;
  --fb-line:#dddfe2;
  --fb-bg:#f5f6f7;
  --fb-text:#1d2129;
  --fb-muted:#4b4f56;
  --fb-blue:#4267b2;
}
*{box-sizing:border-box;margin:0;padding:0}
html,body{width:1200px;height:800px;overflow:hidden}
body{background:var(--stage);font-family:"Oswald",sans-serif;position:relative}
.page{position:absolute;left:174px;top:193px;width:851px;height:415px;background:var(--fb-bg);overflow:hidden}
.cover{position:absolute;left:0;top:0;width:851px;height:315px;background:
  repeating-linear-gradient(135deg,#1b1b1b 0 2px,#121212 2px 4px);overflow:hidden}
.cover-band{position:absolute;inset:0}
.trainer-photo{position:absolute;left:308px;top:5px;width:140px;height:310px;
  background:linear-gradient(180deg,rgba(150,150,150,.55) 0%,#8d8d8d 35%,#6e6e6e 70%,#4a4a4a 100%);
  border-radius:40px 40px 0 0}
.headline{position:absolute;left:16px;top:32px}
.headline-name{font-family:"Bebas Neue",sans-serif;font-size:68px;line-height:62px;letter-spacing:2px;
  background:linear-gradient(180deg,var(--silver-hi) 0%,#d8d8d8 45%,var(--silver-lo) 100%);
  -webkit-background-clip:text;background-clip:text;color:transparent}
.headline-tag{font-family:"Bebas Neue",sans-serif;font-size:26px;color:#e2e2e2;letter-spacing:1px;margin-top:0}
.contact-list{position:absolute;left:566px;top:34px;list-style:none}
.contact-item{display:flex;align-items:center;height:25px;margin-bottom:4px;width:290px;
  background:linear-gradient(90deg,rgba(11,63,126,.9) 0%,rgba(11,63,126,.45) 60%,rgba(11,63,126,0) 100%)}
.contact-icon{width:25px;height:25px;background:var(--icon-blue);display:flex;align-items:center;justify-content:center;flex:none}
.contact-text{font-family:"Oswald",sans-serif;font-weight:700;font-size:9.5px;color:var(--white);margin-left:8px;text-transform:uppercase;letter-spacing:.2px;white-space:nowrap}
.cert-strip{position:absolute;left:518px;top:194px;width:333px;height:60px;background:var(--brand-blue-bright)}
.cert-badge{position:absolute;top:6px;height:50px;background:#f2f2f2}
.cert-badge.dark{background:#111}
.profile{position:absolute;left:13px;top:175px;width:169px;height:169px;background:var(--white);padding:5px;border:1px solid #ccc;z-index:3}
.profile-mark{width:100%;height:100%;background:var(--brand-blue);display:flex;flex-direction:column;align-items:center;justify-content:center;color:var(--white);font-family:"Oswald",sans-serif;font-weight:700}
.profile-initials{font-size:64px;line-height:64px}
.profile-name{font-size:22px;line-height:28px}
.actions{position:absolute;top:274px;display:flex;height:28px;z-index:2}
.btn{background:var(--white);border:1px solid #ccd0d5;font-family:"Noto Sans Bengali",sans-serif;font-weight:600;font-size:14px;color:var(--fb-muted);display:flex;align-items:center;padding:0 10px;gap:5px;white-space:nowrap}
.btn + .btn{border-left:none}
.btn.more{font-size:18px;letter-spacing:-1px;width:42px;justify-content:center;padding:0}
.nav{position:absolute;left:0;top:315px;width:851px;height:44px;background:var(--white);border-bottom:1px solid var(--fb-line)}
.nav-tabs{position:absolute;left:196px;top:0;display:flex;height:44px;list-style:none;font-family:"Noto Sans Bengali",sans-serif;font-size:15px;color:var(--fb-muted)}
.nav-tab{padding:0 15px;display:flex;align-items:center;border-right:1px solid #e9ebee;height:28px;margin-top:8px}
.nav-tab.active{color:var(--fb-text);font-weight:600;border-bottom:2px solid var(--fb-blue);height:36px;margin-top:8px;padding-bottom:6px}
.nav-tab:last-child{border-right:none}
.side-card{position:absolute;left:0;top:371px;width:343px;height:50px;background:var(--white);border:1px solid var(--fb-line)}
.side-title{font-family:"Noto Sans Bengali",sans-serif;font-weight:600;font-size:15px;color:var(--fb-muted);position:absolute;left:10px;top:4px}
.composer{position:absolute;left:355px;top:371px;width:500px;height:50px;background:var(--white);border:1px solid var(--fb-line)}
.composer-tabs{display:flex;gap:12px;padding:4px 10px;font-family:"Noto Sans Bengali",sans-serif;font-weight:600;font-size:15px;color:var(--fb-text);border-bottom:1px solid var(--fb-line);height:36px;align-items:center}
.composer-tab{display:flex;align-items:center;gap:6px}
.tab-icon{width:16px;height:16px;display:inline-block}
</style>
</head>
<body>
<main class="page">
  <section class="cover">
    <svg class="cover-band" width="851" height="315" viewBox="0 0 851 315" aria-hidden="true">
      <defs>
        <pattern id="band-lines" width="4" height="4" patternUnits="userSpaceOnUse" patternTransform="rotate(45)">
          <rect width="4" height="4" fill="#0b3f7e"/><rect width="1.5" height="4" fill="#0e4689"/>
        </pattern>
      </defs>
      <polygon points="310,0 588,0 273,315 0,315 0,310" fill="url(#band-lines)"/>
    </svg>

    <div class="trainer-photo" role="img" aria-label="Photo of two fit trainers standing side by side"></div>

    <div class="headline">
      <h1 class="headline-name">LEV DUNMORE</h1>
      <p class="headline-tag">- YOUR HOME PERSONAL TRAINER -</p>
    </div>

    <ul class="contact-list">
      <li class="contact-item">
        <span class="contact-icon"><svg width="15" height="14" viewBox="0 0 15 14"><path d="M7.5 1 1 7h2v6h3.5V9h2v4H12V7h2z" fill="#fff"/></svg></span>
        <span class="contact-text">47 Valmorin, Havre-Loriot, Belcourt, K7R 2P4</span>
      </li>
      <li class="contact-item">
        <span class="contact-icon"><svg width="15" height="11" viewBox="0 0 15 11"><rect x=".5" y=".5" width="14" height="10" fill="#fff"/><path d="M1 1l6.5 5L14 1" stroke="#1a4f90" stroke-width="1.4" fill="none"/></svg></span>
        <span class="contact-text">ldstrongdaily@mailbox.example</span>
      </li>
      <li class="contact-item">
        <span class="contact-icon"><svg width="14" height="14" viewBox="0 0 14 14"><path d="M3 1l2.5 3-1.5 1.6c.8 1.8 2.2 3.2 4 4L9.6 8 13 10.5 11.4 13C6 12.6 1.4 8 1 2.6z" fill="#fff"/></svg></span>
        <span class="contact-text">555.204-3917</span>
      </li>
      <li class="contact-item">
        <span class="contact-icon"><svg width="12" height="12" viewBox="0 0 12 12"><circle cx="6" cy="6" r="5.5" fill="#fff"/></svg></span>
        <span class="contact-text">www.chirper.example/LDStrongDaily</span>
      </li>
      <li class="contact-item">
        <span class="contact-icon"><svg width="14" height="14" viewBox="0 0 14 14"><g fill="none" stroke="#fff" stroke-width="2"><rect x="1.5" y="5.5" width="6" height="4" rx="2" transform="rotate(-45 4.5 7.5)"/><rect x="6.5" y="4.5" width="6" height="4" rx="2" transform="rotate(-45 9.5 6.5)"/></g></svg></span>
        <span class="contact-text">www.BougeAvecToi.example</span>
      </li>
    </ul>

    <div class="cert-strip" aria-label="Certifications">
      <div class="cert-badge" style="left:20px;width:50px"></div>
      <div class="cert-badge dark" style="left:78px;width:100px"></div>
      <div class="cert-badge" style="left:188px;width:60px"></div>
      <div class="cert-badge" style="left:258px;width:60px"></div>
    </div>

    <div class="actions" style="left:463px">
      <span class="btn"><svg width="13" height="13" viewBox="0 0 13 13"><path d="M1 6h2.5v6H1zM4.5 6l3-5c1 0 1.6.8 1.3 2L8.3 5H12l-1.2 7H4.5z" fill="#4267b2"/></svg>পছন্দকৃত ▾</span>
    </div>
    <div class="actions" style="left:586px">
      <span class="btn"><svg width="12" height="10" viewBox="0 0 12 10"><path d="M1 5l3.5 3.5L11 1" stroke="#4b4f56" stroke-width="2" fill="none"/></svg>অনুসরণ করছেন</span>
      <span class="btn"><svg width="12" height="11" viewBox="0 0 12 11"><path d="M1 1h10v7H5l-3 2.5V8H1z" fill="#4b4f56"/></svg>বার্তা</span>
      <span class="btn more">•••</span>
    </div>
  </section>

  <div class="profile">
    <div class="profile-mark">
      <span class="profile-initials">LD</span>
      <span class="profile-name">StrongDaily</span>
    </div>
  </div>

  <nav class="nav">
    <ul class="nav-tabs">
      <li class="nav-tab active">টাইমলাইন</li>
      <li class="nav-tab">সম্বন্ধে</li>
      <li class="nav-tab">চিত্রসম্ভার</li>
      <li class="nav-tab">পছন্দ</li>
      <li class="nav-tab">আরও ▾</li>
    </ul>
  </nav>

  <aside class="side-card">
    <span class="side-title">লোকজন</span>
    <svg style="position:absolute;right:12px;top:12px" width="8" height="12" viewBox="0 0 8 12"><path d="M1 1l5 5-5 5" stroke="#4b4f56" stroke-width="2" fill="none"/></svg>
  </aside>

  <section class="composer">
    <div class="composer-tabs">
      <span class="composer-tab"><svg class="tab-icon" viewBox="0 0 16 16"><rect width="16" height="16" rx="2" fill="#4267b2"/><path d="M4 12l1-3 5-5 2 2-5 5z" fill="#fff"/></svg>পোস্ট</span>
      <span class="composer-tab"><svg class="tab-icon" viewBox="0 0 16 16"><rect x="1" y="1" width="14" height="14" rx="2" fill="none" stroke="#e9822e" stroke-width="2"/><path d="M4 12l3-4 2 2 1.5-1.5L12 12z" fill="#e9822e"/></svg>ছবি/ভিডিও</span>
    </div>
  </section>
</main>
</body>
</html>
```